Professional Business Card for Luxury Hotel & Resort Development Firm. Advisory firm

Project Overview: We are a specialized advisory firm focused on Hotel & Resort Development. Our clients are high-net-worth investors and major hospitality brands.

Design Requirements:

Style: Minimalist, sophisticated, and trustworthy. We want to avoid looking too "corporate" or "dry"—it should feel premium.

Key Elements: Please incorporate our logo [もしロゴがあれば] and emphasize a clean layout with plenty of white space.

Color Palette: We prefer Grey and White or Black and White to evoke a sense of luxury and stability.

Typography: Professional garamond, or sans-serif or elegant serif fonts

Goal: The card should feel substantial and high-end when handed to a client, reflecting our expertise in multi-million dollar developments.
Updates

I am currently on a business trip for field research and have limited access to my desktop. Additionally, I have just provided detailed technical feedback to a designer and am waiting for their refined proposals. To ensure the final logo meets the high standards of my new advisory firm, I would like to extend the deadline by 7 days. Thank you for your support.

Target Market(s)

High-net-worth investors, luxury hospitality brands, and real estate developers.

Contact Information for Business Card

Firm Name: Harbor Crest Partners, My Name: Kenji Morisawa, Title: Founder, Address 5-8-4 Kitanomura Aoba Yokohama Japan 225-0143, email address: kmorisawa@harborcrestpx.example, Tel: +81 90-4183-2750. Front Site (Primary): Japanese translation of the back side, Please use a clean Japanese font (like Mincho) that complements the Garmond on the English side Back side: English. Note for Japanese text: since the frond side is the main fae, please ensure the layout is clean and professional. Please use a high-quality Mincho ( Serif-style) font for Japanese to mach the Garmond used on the English side. Text for Front side (Japanese) Harbor Crest Partners, 役職:代表、森沢健二、225-0143 横浜市青葉区北野村5-8-4. Name of the firm can stay in English.

Font styles to use
Other font styles liked:
• Font Preference: Please use Garamond for all text to maintain a consistent, elegant, and classic professional look.

Requirements
Must have
• Professional and clean layout, high-end feel.
Nice to have
• Minimalist design with subtle luxury accents.

```html
<!DOCTYPE html>
<html lang="en">
<head>
<meta charset="utf-8">
<title>Kenji Morisawa – Business Card</title>
<link rel="stylesheet" href="https://fonts.googleapis.com/css2?family=Kumbh+Sans:wght@400;600;700&display=swap">
<style>
  :root {
    --page-bg: #e4e4e4;
    --card-black: #040405;
    --accent-band: #3a3a3c;
    --contact-panel: #6d6e72;
    --name-grey: #6f7074;
    --ink: #0c0c0d;
    --pattern-dark: #09090a;
    --pattern-light: #19191b;
  }
  * { margin: 0; padding: 0; box-sizing: border-box; }
  html, body {
    width: 1200px;
    height: 1200px;
    overflow: hidden;
    background: var(--page-bg);
    font-family: "Kumbh Sans", sans-serif;
  }
  .business-card {
    position: absolute;
    left: 50px;
    top: 286px;
    width: 1100px;
    height: 628px;
    background: var(--card-black);
    overflow: hidden;
  }
  .pattern-field {
    position: absolute;
    left: 520px;
    top: 0;
    width: 580px;
    height: 628px;
    background: linear-gradient(110deg, var(--card-black) 0%, var(--pattern-dark) 35%, var(--pattern-light) 100%);
  }
  .accent-band {
    position: absolute;
    left: 50px;
    top: 0;
    width: 73px;
    height: 265px;
    background: var(--accent-band);
  }
  .identity {
    position: absolute;
    left: 170px;
    top: 82px;
    color: var(--name-grey);
  }
  .identity__name {
    font-size: 46px;
    font-weight: 700;
    letter-spacing: 0.6px;
    line-height: 1.1;
  }
  .identity__title {
    font-size: 31px;
    font-weight: 400;
    letter-spacing: 1.2px;
    line-height: 1.3;
    margin-top: 2px;
  }
  .contact-panel {
    position: absolute;
    left: 0;
    top: 265px;
    width: 788px;
    height: 293px;
    background: var(--contact-panel);
  }
  .contact-list {
    list-style: none;
    position: absolute;
    left: 70px;
    top: 58px;
    color: var(--ink);
    font-size: 29px;
    line-height: 44.5px;
    letter-spacing: 0.5px;
  }
  .contact-list li {
    display: flex;
    align-items: flex-start;
  }
  .contact-list .icon {
    width: 22px;
    height: 22px;
    margin-top: 10px;
    margin-right: 30px;
    flex: none;
    fill: var(--ink);
  }
  .contact-list .phone { font-weight: 600; }
  .contact-list .address-line2 { padding-left: 52px; }
</style>
</head>
<body>
  <div class="business-card">
    <div class="pattern-field" role="img" aria-label="Subtle dark geometric line pattern decoration"></div>
    <div class="accent-band"></div>

    <div class="identity">
      <h1 class="identity__name">Kenji Morisawa</h1>
      <p class="identity__title">Founder</p>
    </div>

    <div class="contact-panel">
      <ul class="contact-list">
        <li class="phone">
          <svg class="icon" viewBox="0 0 24 24" aria-hidden="true"><path d="M6.6 10.8a15.1 15.1 0 0 0 6.6 6.6l2.2-2.2c.3-.3.7-.4 1-.2 1.1.4 2.3.6 3.6.6.6 0 1 .4 1 1V20c0 .6-.4 1-1 1A17 17 0 0 1 3 4c0-.6.4-1 1-1h3.5c.6 0 1 .4 1 1 0 1.3.2 2.5.6 3.6.1.3 0 .7-.2 1z"/></svg>
          <span>+81 90-4183-2750.</span>
        </li>
        <li>
          <svg class="icon" viewBox="0 0 24 24" aria-hidden="true"><path d="M2 5h20v14H2zM4 7v.5l8 5 8-5V7l-8 5z"/></svg>
          <span>kmorisawa@harborcrestpx.example</span>
        </li>
        <li>
          <svg class="icon" viewBox="0 0 24 24" aria-hidden="true"><path d="M12 2a7 7 0 0 0-7 7c0 5.2 7 13 7 13s7-7.8 7-13a7 7 0 0 0-7-7zm0 9.5A2.5 2.5 0 1 1 12 6.5a2.5 2.5 0 0 1 0 5z"/></svg>
          <span>5-8-4 Kitanomura Aoba Yokohama</span>
        </li>
        <li class="address-line2"><span>Japan 225-0143</span></li>
      </ul>
    </div>
  </div>
</body>
</html>
```